Velmora Grid - Stock Certificate

We need a custom designed stock certificate that represents the look of our company logo but also have a cool look compared to a standard stock certificate. We thinking we want the logo in gold. Our website is https://www.velmoragridusa.example.

We are wanting the certificate to look very professional and really cool, we have sales agents that work for the company and we are creating a program by which the sales agents can gain ownership in the company. So the certificates need to have a very cool appeal and that provides a sense of pride in owning "Units" in Velmora Grid.
Updates

Project Deadline Extended
Reason: Extending so other board members can vote as well, thank you all!

Target Market(s)

Stock/Shareholders

Industry/Entity Type

It Company

Font styles to use
Script

Requirements
Must have
• Must look like a stock certificate, must use our logo which the psd file for it was attached.
Nice to have
• Nice to have the logo in gold

```html
<!DOCTYPE html>
<html lang="en">
<head>
<meta charset="utf-8">
<title>Velmora Grid – Unit Certificate</title>
<link rel="stylesheet" href="https://fonts.googleapis.com/css2?family=Open+Sans:ital,wght@0,400;0,600;0,800;1,700&display=swap">
<style>
  :root {
    --ink: #231f20;
    --paper: #ececec;
    --paper-light: #f6f6f6;
    --paper-shade: #dcdcdc;
    --panel-black: #151515;
    --panel-grey: #2c2c2c;
    --orange: #e0601f;
    --orange-deep: #c2461a;
    --gold: #f6b530;
    --gold-light: #fde08a;
    --brand-gold: #f3c04e;
  }
  * { margin: 0; padding: 0; box-sizing: border-box; }
  html, body { width: 1200px; height: 927px; overflow: hidden; background: var(--paper); }
  .certificate {
    position: relative;
    width: 1200px;
    height: 927px;
    overflow: hidden;
    font-family: "Open Sans", Arial, sans-serif;
    color: var(--ink);
    background: linear-gradient(160deg, var(--paper-light) 0%, var(--paper) 55%, var(--paper-shade) 100%);
  }
  .backdrop { position: absolute; inset: 0; width: 1200px; height: 927px; }
  .brand-name {
    position: absolute;
    left: 68px;
    top: 272px;
    font-size: 40px;
    font-weight: 600;
    letter-spacing: 1px;
    color: var(--brand-gold);
    white-space: nowrap;
  }
  .title {
    position: absolute;
    left: 549px;
    top: 124px;
    font-size: 66px;
    font-weight: 800;
    letter-spacing: -1px;
    line-height: 1;
  }
  .subtitle {
    position: absolute;
    left: 638px;
    top: 193px;
    width: 410px;
    font-size: 44px;
    font-weight: 400;
    letter-spacing: -0.5px;
    line-height: 1;
    white-space: nowrap;
  }
  .presented {
    position: absolute;
    left: 458px;
    width: 700px;
    top: 311px;
    text-align: center;
    font-size: 18px;
  }
  .recipient {
    position: absolute;
    left: 418px;
    width: 780px;
    top: 374px;
    text-align: center;
    font-size: 74px;
    font-weight: 700;
    font-style: italic;
    letter-spacing: -1px;
    line-height: 1.1;
  }
  .tagline {
    position: absolute;
    left: 438px;
    width: 740px;
    top: 513px;
    text-align: center;
    font-size: 19px;
  }
  .statement {
    position: absolute;
    left: 465px;
    width: 663px;
    top: 581px;
    font-size: 15px;
    line-height: 22px;
    text-align: justify;
  }
  .sign-field {
    position: absolute;
    top: 808px;
    border-top: 1.5px solid var(--ink);
    padding-top: 8px;
    text-align: center;
    font-size: 18px;
  }
  .sign-field.date { left: 447px; width: 192px; }
  .sign-field.signature { left: 741px; width: 322px; }
</style>
</head>
<body>
<main class="certificate">
  <svg class="backdrop" viewBox="0 0 1200 927" xmlns="http://www.w3.org/2000/svg">
    <defs>
      <linearGradient id="sideBand" x1="0" y1="0" x2="0" y2="1">
        <stop offset="0" stop-color="#f9c74a"/>
        <stop offset="0.5" stop-color="#fde7a0"/>
        <stop offset="1" stop-color="#f7b733"/>
      </linearGradient>
      <radialGradient id="panelShade" cx="0.45" cy="0.35" r="0.75">
        <stop offset="0" stop-color="var(--panel-grey)"/>
        <stop offset="1" stop-color="var(--panel-black)"/>
      </radialGradient>
      <radialGradient id="emblemGlow" cx="0.5" cy="0.5" r="0.5">
        <stop offset="0" stop-color="#fbd35a"/>
        <stop offset="0.35" stop-color="#d68a2a"/>
        <stop offset="0.7" stop-color="#7a3e14" stop-opacity="0.8"/>
        <stop offset="1" stop-color="#151515" stop-opacity="0"/>
      </radialGradient>
      <radialGradient id="goldDot" cx="0.35" cy="0.35" r="0.7">
        <stop offset="0" stop-color="var(--gold-light)"/>
        <stop offset="1" stop-color="var(--orange)"/>
      </radialGradient>
    </defs>

    <path d="M380 480 C 600 330, 820 420, 900 927 L 380 927 Z" fill="#dedede" opacity="0.6"/>
    <path d="M700 300 C 900 150, 1150 300, 1200 520 L 1200 927 L 1040 927 C 1000 650, 900 420, 700 300 Z" fill="#e2e2e2" opacity="0.7"/>

    <rect x="0" y="0" width="381" height="927" fill="url(#sideBand)"/>

    <ellipse cx="165" cy="470" rx="245" ry="485" fill="var(--orange-deep)"/>
    <ellipse cx="160" cy="470" rx="235" ry="476" fill="var(--gold)"/>
    <ellipse cx="155" cy="470" rx="228" ry="470" fill="var(--orange)"/>
    <ellipse cx="148" cy="470" rx="220" ry="464" fill="url(#panelShade)"/>

    <circle cx="182" cy="591" r="150" fill="url(#emblemGlow)" role="img" aria-label="Glowing gold emblem illustration"/>

    <circle cx="384" cy="776" r="31" fill="url(#goldDot)"/>
  </svg>

  <div class="brand-name">Velmora Grid</div>

  <h1 class="title">CERTIFICATE</h1>
  <p class="subtitle">OF UNIT OWNERSHIP</p>
  <p class="presented">CERTIFICATE No. VG-0001 &nbsp;·&nbsp; THIS CERTIFIES THAT</p>
  <p class="recipient">Name Surname</p>
  <p class="tagline">is the registered holder of 1,000 fully paid Units of Velmora Grid</p>
  <p class="statement">The Units represented by this certificate are held by the shareholder named above and are transferable only on the books of Velmora Grid by the holder in person or by a duly authorized attorney upon surrender of this certificate properly endorsed. This certificate is issued under the ownership program for sales agents and is subject to the operating agreement of the company, as amended from time to time. In witness whereof, the company has caused this certificate to be signed by its duly authorized officer on the date below. www.velmoragridusa.example</p>

  <div class="sign-field date">DATE</div>
  <div class="sign-field signature">SIGNATURE</div>
</main>
</body>
</html>
```